Vessa Almond Protein - Less, but better

Design a protein powder pouch (350g). Take inspiration from Brimora.co and put the same information on the pouch and add "made in Australia". I do not want it to be exactly the same design but just take some inspiration from it.

```html
<!DOCTYPE html>
<html lang="en">
<head>
<meta charset="UTF-8">
<title>Vessa Almond Protein Powder – Pouch Label</title>
<link rel="stylesheet" href="https://fonts.googleapis.com/css2?family=Outfit:wght@400;500&family=Quicksand:wght@500;600;700&family=Montserrat:wght@700;800&display=swap">
<style>
  :root {
    --page-bg: #f1f1f0;
    --orange: #f0a420;
    --sage: #7a9e91;
    --blush: #e5a59d;
    --cream: #fbf8ea;
    --forest: #1b3a33;
  }
  * { margin: 0; padding: 0; box-sizing: border-box; }
  html, body {
    width: 1200px;
    height: 825px;
    overflow: hidden;
    background: var(--page-bg);
  }
  .label {
    position: absolute;
    left: 301px;
    top: 22px;
    width: 597px;
    height: 780px;
    overflow: hidden;
    color: var(--cream);
  }
  .label-bg { position: absolute; inset: 0; display: block; }

  .brand-name {
    position: absolute;
    top: 118px;
    left: 0;
    width: 100%;
    text-align: center;
    font-family: "Quicksand", sans-serif;
    font-weight: 700;
    font-size: 104px;
    line-height: 1;
    letter-spacing: -1px;
    color: var(--cream);
  }
  .tagline {
    position: absolute;
    top: 232px;
    left: 0;
    width: 100%;
    text-align: center;
    font-family: "Quicksand", sans-serif;
    font-weight: 500;
    font-size: 22px;
    letter-spacing: 2px;
  }

  .product-card {
    position: absolute;
    left: 131px;
    top: 317px;
    width: 336px;
    height: 319px;
    background: var(--cream);
    border-radius: 20px;
  }
  .product-title {
    position: absolute;
    top: 22px;
    left: 0;
    width: 100%;
    text-align: center;
    font-family: "Outfit", sans-serif;
    font-weight: 500;
    font-size: 71px;
    line-height: 65px;
    letter-spacing: -2px;
    color: var(--sage);
  }
  .flavour-bar {
    position: absolute;
    left: 27px;
    top: 227px;
    width: 282px;
    height: 34px;
    background: var(--blush);
    font-family: "Montserrat", sans-serif;
    font-weight: 800;
    font-size: 19px;
    letter-spacing: 6px;
    line-height: 34px;
    text-align: center;
    color: var(--cream);
  }
  .product-points {
    position: absolute;
    top: 274px;
    left: 0;
    width: 100%;
    text-align: center;
    font-family: "Outfit", sans-serif;
    font-weight: 400;
    font-size: 16.5px;
    color: var(--sage);
  }

  .benefits {
    position: absolute;
    top: 654px;
    left: 0;
    width: 100%;
    text-align: center;
    font-family: "Quicksand", sans-serif;
    font-weight: 500;
    font-size: 18.5px;
    line-height: 24px;
    letter-spacing: 2.4px;
  }
  .origin {
    position: absolute;
    top: 729px;
    left: 0;
    width: 100%;
    text-align: center;
    font-family: "Outfit", sans-serif;
    font-weight: 400;
    font-size: 17.5px;
    letter-spacing: 3px;
  }
  .net-weight {
    position: absolute;
    top: 753px;
    left: 0;
    width: 100%;
    text-align: center;
    font-family: "Montserrat", sans-serif;
    font-weight: 700;
    font-size: 14px;
    letter-spacing: 1.5px;
  }
</style>
</head>
<body>
  <main class="label">
    <svg class="label-bg" viewBox="0 0 597 780" width="597" height="780" aria-hidden="true">
      <rect x="0" y="0" width="597" height="780" fill="var(--blush)"/>
      <path d="M0 0 H597 V268 C520 272 440 288 330 285 C230 283 150 270 90 272 C45 273 20 278 0 282 Z" fill="var(--sage)"/>
      <rect x="0" y="0" width="597" height="90" fill="var(--orange)"/>
      <circle cx="641" cy="830" r="181" fill="var(--sage)"/>
      <circle cx="621" cy="856" r="147" fill="var(--forest)"/>
    </svg>

    <div class="brand-name">vessa</div>
    <p class="tagline">– less, but better –</p>

    <section class="product-card">
      <h1 class="product-title">ALMOND<br>PROTEIN<br>POWDER</h1>
      <div class="flavour-bar">REAL VANILLA</div>
      <p class="product-points">Vegan • 4 Ingredients • Easy Mix</p>
    </section>

    <p class="benefits">Muscle Support • Digestive Health<br>Skin Health • Longevity</p>
    <p class="origin">MADE IN AUSTRALIA</p>
    <p class="net-weight">Net Wt. 350g</p>
  </main>
</body>
</html>
```